Personal letterhead and stationary

I am looking for someone to design letterhead and stationary set for my personal use. I want something simple and timeless with a little bit of color. I like photography, computers and writing.

```html
<!DOCTYPE html>
<html lang="en">
<head>
<meta charset="utf-8">
<title>Daniel Ross Hartley — Letterhead</title>
<link href="https://fonts.googleapis.com/css2?family=Josefin+Sans:wght@400;600&display=swap" rel="stylesheet">
<style>
  :root {
    --green: #8aad5a;
    --green-pale: #d6e3c2;
    --ink: #111111;
    --paper: #fdfdfb;
    --page-edge: #c8c8c8;
    --bg: #ffffff;
  }
  * { box-sizing: border-box; margin: 0; padding: 0; }
  html, body { width: 1200px; height: 1000px; overflow: hidden; background: var(--bg); }
  body { position: relative; font-family: "Josefin Sans", Arial, sans-serif; color: var(--ink); }

  .stripe-band { position: absolute; background: var(--green-pale); }

  .masthead {
    position: absolute;
    background: #fff;
    border: 3px solid var(--green);
    display: grid;
  }
  .masthead__name {
    display: flex; align-items: center;
    border-bottom: 3px solid var(--green);
    text-transform: uppercase;
    font-weight: 600;
    white-space: nowrap;
  }
  .masthead__contact { display: grid; }
  .contact-cell {
    display: flex; align-items: center;
    text-transform: uppercase;
    white-space: nowrap;
  }
  .contact-cell--phone { border-left: 3px solid var(--green); }
  .contact-cell svg { flex: none; }

  /* Large header detail */
  .detail .stripe-band { left: 0; top: 0; width: 1200px; height: 268px; }
  .detail .masthead { left: 116px; top: 69px; width: 968px; height: 151px; grid-template-rows: 89px 1fr; }
  .detail .masthead__name { font-size: 50px; letter-spacing: 0.36em; padding-left: 28px; padding-top: 8px; }
  .detail .masthead__contact { grid-template-columns: 709px 1fr; }
  .detail .contact-cell { font-size: 14px; letter-spacing: 0.26em; padding-top: 3px; }
  .detail .contact-cell--address { padding-left: 25px; gap: 22px; }
  .detail .contact-cell--phone { padding-left: 24px; gap: 22px; }

  /* Letter sheet */
  .sheet {
    position: absolute; left: 607px; top: 494px; width: 469px; height: 520px;
    background: var(--paper); border: 1px solid var(--page-edge);
  }
  .sheet .stripe-band { left: 0; top: 0; width: 467px; height: 104px; }
  .sheet .masthead { left: 43px; top: 26px; width: 381px; height: 61px; border-width: 2px; grid-template-rows: 34px 1fr; }
  .sheet .masthead__name { font-size: 19px; letter-spacing: 0.34em; padding-left: 10px; padding-top: 3px; border-bottom-width: 2px; }
  .sheet .masthead__contact { grid-template-columns: 278px 1fr; }
  .sheet .contact-cell { font-size: 6px; letter-spacing: 0.2em; padding-top: 1px; }
  .sheet .contact-cell--address { padding-left: 9px; gap: 8px; }
  .sheet .contact-cell--phone { padding-left: 8px; gap: 7px; border-left-width: 2px; }
</style>
</head>
<body>

<section class="detail">
  <div class="stripe-band" role="img" aria-label="Green diagonal stripe pattern band"></div>
  <header class="masthead">
    <div class="masthead__name">Daniel Ross Hartley</div>
    <div class="masthead__contact">
      <div class="contact-cell contact-cell--address">
        <svg width="35" height="24" viewBox="0 0 35 24" aria-hidden="true"><rect x="0.75" y="0.75" width="33.5" height="22.5" fill="none" stroke="#111" stroke-width="1.5"/><path d="M1 1 L17.5 13 L34 1 M1 23 L13 11 M34 23 L22 11" fill="none" stroke="#111" stroke-width="1.2"/><circle cx="17.5" cy="12" r="4" fill="#111"/></svg>
        <span>2750 Shutterfield Road, San Francisco, CA 94612</span>
      </div>
      <div class="contact-cell contact-cell--phone">
        <svg width="34" height="26" viewBox="0 0 34 26" aria-hidden="true"><path d="M2 8 C2 2 32 2 32 8 L32 10 L25 10 L25 7 L9 7 L9 10 L2 10 Z" fill="#111"/><path d="M10 9 L24 9 L29 24 L5 24 Z" fill="#111"/><circle cx="17" cy="17" r="4.5" fill="#fff"/><circle cx="17" cy="17" r="1.8" fill="#111"/></svg>
        <span>415 555 0182</span>
      </div>
    </div>
  </header>
</section>

<section class="sheet">
  <div class="stripe-band" role="img" aria-label="Green diagonal stripe pattern band"></div>
  <header class="masthead">
    <div class="masthead__name">Daniel Ross Hartley</div>
    <div class="masthead__contact">
      <div class="contact-cell contact-cell--address">
        <svg width="14" height="10" viewBox="0 0 35 24" aria-hidden="true"><rect x="0.75" y="0.75" width="33.5" height="22.5" fill="none" stroke="#111" stroke-width="2"/><path d="M1 1 L17.5 13 L34 1 M1 23 L13 11 M34 23 L22 11" fill="none" stroke="#111" stroke-width="1.6"/><circle cx="17.5" cy="12" r="4" fill="#111"/></svg>
        <span>2750 Shutterfield Road, San Francisco, CA 94612</span>
      </div>
      <div class="contact-cell contact-cell--phone">
        <svg width="13" height="10" viewBox="0 0 34 26" aria-hidden="true"><path d="M2 8 C2 2 32 2 32 8 L32 10 L25 10 L25 7 L9 7 L9 10 L2 10 Z" fill="#111"/><path d="M10 9 L24 9 L29 24 L5 24 Z" fill="#111"/><circle cx="17" cy="17" r="4.5" fill="#fff"/></svg>
        <span>415 555 0182</span>
      </div>
    </div>
  </header>
</section>

</body>
</html>
```